International Medical Company Needs a Website Design for a Support Site

We need a website design for a support site we are doing for ostomates called Bright Returns. We are an international company but this website is for our Australian market.

The website is a support site for people who are living with an Ostomy or Bowel Disease. This is a site where they can read other ostomates' stories and how they are dealing with the fact that they have to wear a pouch everyday.

The URL for our US site is: http://www.brightreturnsvale.com/

We need to use the same logo but we have freedom around the color scheme. We are not fond of the brown color scheme used in our US site and are happy for designs to be submitted with alternatives.

• We want the design to be clean, inspiring, modern and inviting.
• We would like to see a design for the mainpage / homepage and one of the subpages
• We only require the PSD / image files (no HTML needed)

Attached to this project is our sitemap, an example wireframe and the logos. We are happy for you to play around with different options and don't have to stick to the layout shown in the wireframe.

If you have any further questions please ask.

```html
<!DOCTYPE html>
<html lang="en">
<head>
<meta charset="utf-8">
<title>Bright Returns – Sharing stories and giving hope</title>
<link href="https://fonts.googleapis.com/css2?family=Open+Sans:wght@400;600;700&display=swap" rel="stylesheet">
<style>
:root{
  --brown:#a0683a;
  --teal:#2bb3bd;
  --teal-dark:#1d98a2;
  --teal-light:#4fc7cf;
  --blue-band:#2c97d3;
  --card-border:#d6dde2;
  --title-blue:#2b8ac2;
  --text:#333;
  --footer:#2d2d2d;
  --footer-line:#3e3e3e;
  --footer-text:#cfcfcf;
  --copy-bg:#0e0e0e;
  --mark:#eceef0;
}
*{box-sizing:border-box;margin:0;padding:0}
html,body{width:1200px;height:1002px;overflow:hidden}
body{font-family:"Open Sans",Arial,sans-serif;color:var(--text);background:#fff;position:relative}
.top-rule{position:absolute;top:0;left:0;width:1200px;height:5px;background:var(--brown)}
.site-header{position:absolute;top:5px;left:0;width:1200px;height:101px;background:#fff}
.brand{position:absolute;left:190px;top:34px;display:flex;align-items:center;gap:8px;font-size:15px;font-weight:600;color:var(--brown);letter-spacing:.5px}
.brand-dot{width:14px;height:14px;border-radius:50%;background:var(--brown)}
.header-actions{position:absolute;top:34px;left:756px;display:flex;gap:6px}
.btn-small{height:27px;border-radius:3px;font-size:12px;display:flex;align-items:center;justify-content:center}
.btn-share{width:148px;background:linear-gradient(var(--teal-light),var(--teal-dark));color:#fff}
.btn-country{width:100px;background:linear-gradient(#f7f7f7,#e2e2e2);border:1px solid #ccc;color:#666;gap:10px}
.main-nav{position:absolute;top:106px;left:0;width:1200px;height:38px;background:linear-gradient(var(--teal-light),var(--teal-dark));display:flex;align-items:stretch;padding-left:190px}
.main-nav a{color:#fff;text-decoration:none;font-size:15px;font-weight:600;display:flex;align-items:center;padding:0 19px;border-right:1px solid rgba(255,255,255,.25)}
.main-nav a.active{background:var(--brown);padding:0 20px}
.nav-search{display:flex;align-items:center;padding:0 26px}
.hero{position:absolute;top:144px;left:0;width:1200px;height:441px}
.hero-photo{position:absolute;inset:0;background:linear-gradient(90deg,#9b8a9c 0%,#c7b8c6 30%,#d9c9cf 55%,#b97a72 75%,#c9bcc8 100%)}
.hero-copy{position:absolute;left:190px;top:100px;color:#fff;text-shadow:0 1px 3px rgba(0,0,0,.45)}
.hero-copy h1{font-size:31px;font-weight:600;margin-bottom:12px}
.hero-copy p{font-size:19px;line-height:24px;width:460px}
.hero-actions{position:absolute;left:190px;top:260px;display:flex;gap:9px}
.btn-hero{width:182px;height:36px;border-radius:3px;background:linear-gradient(var(--teal-light),var(--teal-dark));color:#fff;font-size:15px;font-weight:600;display:flex;align-items:center;justify-content:center}
.feature-band{position:absolute;top:585px;left:0;width:1200px;height:281px;background:var(--blue-band)}
.card{position:absolute;top:38px;width:264px;height:202px;background:#fff;border:5px solid var(--card-border);padding:12px 16px 0;overflow:hidden}
.card h2{position:relative;z-index:1;font-size:16px;font-weight:600;color:var(--title-blue);margin-bottom:3px}
.card-body{position:relative;z-index:1;font-size:11px;line-height:16px;letter-spacing:-.1px;color:#222;height:112px;overflow:hidden}
.card-mark{position:absolute;z-index:0;left:16px;bottom:20px;font-size:22px;font-weight:700;color:var(--mark);letter-spacing:1px;white-space:nowrap}
.card-pager{position:absolute;z-index:1;bottom:7px;left:0;width:100%;display:flex;justify-content:center;gap:6px}
.card-pager span{width:11px;height:11px;border-radius:50%;background:var(--teal-dark)}
.story-thumb{float:right;width:100px;height:64px;margin:2px 0 4px 8px;background:linear-gradient(135deg,#2e6fb5,#7fb3de)}
.news-list{position:relative;z-index:1;margin-top:4px}
.news-item{font-size:11px;line-height:16px;letter-spacing:-.1px;height:42px;padding-top:2px;overflow:hidden;border-bottom:1px solid #ccc;margin-bottom:5px}
.news-item:last-child{border-bottom:0;margin-bottom:0;height:36px}
.site-footer{position:absolute;top:866px;left:0;width:1200px;height:136px;background:var(--footer)}
.footer-title{position:absolute;top:25px;font-size:14px;color:var(--teal)}
.quick-links{position:absolute;left:190px;top:66px;display:flex;font-size:11.5px;color:var(--footer-text)}
.quick-links a{color:inherit;text-decoration:none;padding:0 13px;border-left:1px solid #777}
.quick-links a:first-child{padding-left:0;border-left:0}
.footer-rule{position:absolute;top:52px;height:1px;background:var(--footer-line)}
.social{position:absolute;left:784px;top:65px;display:flex;gap:8px}
.social span{width:24px;height:24px;border-radius:2px}
.copyright{position:absolute;bottom:0;left:0;width:1200px;height:23px;background:var(--copy-bg);color:#ddd;font-size:10.5px;padding-left:190px;display:flex;align-items:center}
</style>
</head>
<body>
<div class="top-rule"></div>
<header class="site-header">
  <div class="brand"><span class="brand-dot"></span>Bright Returns</div>
  <div class="header-actions">
    <div class="btn-small btn-share">Share a Story</div>
    <div class="btn-small btn-country">Country
      <svg width="8" height="6" viewBox="0 0 8 6"><path d="M0 0h8L4 6z" fill="#555"/></svg>
    </div>
  </div>
</header>
<nav class="main-nav">
  <a class="active" href="#">Home</a>
  <a href="#">About us</a>
  <a href="#">Personal stories</a>
  <a href="#">Tips for Living</a>
  <a href="#">News</a>
  <a href="#">Resources</a>
  <a href="#">Contact us</a>
  <span class="nav-search">
    <svg width="16" height="16" viewBox="0 0 16 16"><circle cx="6.5" cy="6.5" r="5" fill="none" stroke="#1b7f88" stroke-width="2"/><path d="M10 10l5 5" stroke="#1b7f88" stroke-width="2"/></svg>
  </span>
</nav>
<section class="hero">
  <div class="hero-photo" role="img" aria-label="Photo of a smiling young woman in a bright room, with two people in the soft-focus background"></div>
  <div class="hero-copy">
    <h1>Sharing stories and giving hope</h1>
    <p>to people around the world who are facing inflammatory bowel disease, colorectal cancer, or have had ostomy surgery</p>
  </div>
  <div class="hero-actions">
    <div class="btn-hero">Share a Story</div>
    <div class="btn-hero">Read Story</div>
  </div>
</section>
<section class="feature-band">
  <article class="card" style="left:190px">
    <div class="card-mark">BRIGHT RETURNS</div>
    <h2>What is Bright Returns</h2>
    <p class="card-body">Lorem Ipsum is simply dummy text of the printing and typesetting industry. Lorem Ipsum has been the industry's standard dummy text ever since the 1500s, when an unknown printer took a galley of type and scrambled it to make a type specimen book. It has survived not only five centuries, but</p>
    <div class="card-pager"><span></span><span></span></div>
  </article>
  <article class="card" style="left:468px">
    <div class="card-mark">BRIGHT RETURNS</div>
    <h2>Share a Story</h2>
    <div class="card-body">
      <div class="story-thumb" role="img" aria-label="Brochure cover with a group of people"></div>
      Lorem Ipsum is simply dummy text of the printing and typesetting industry. Lorem Ipsum has been the industry's standard dummy text ever since the 1500s, when an unknown printer took a galley of type and scrambled it to make a
    </div>
    <div class="card-pager"><span></span><span></span></div>
  </article>
  <article class="card" style="left:747px">
    <div class="card-mark">BRIGHT RETURNS</div>
    <h2>News</h2>
    <div class="news-list">
      <div class="news-item">Lorem Ipsum is simply dummy text of the printing and typesetting industry. Lorem</div>
      <div class="news-item">Lorem Ipsum is simply dummy text of the printing and typesetting industry. Lorem</div>
      <div class="news-item">Lorem Ipsum is simply dummy text of the printing and typesetting industry. Lorem</div>
    </div>
    <div class="card-pager"><span></span><span></span></div>
  </article>
</section>
<footer class="site-footer">
  <div class="footer-title" style="left:190px">Quick links</div>
  <div class="footer-rule" style="left:190px;width:540px"></div>
  <div class="quick-links">
    <a href="#">About us</a><a href="#">Personal stories</a><a href="#">Tips for Living</a><a href="#">News</a><a href="#">Resources</a><a href="#">Contact us</a>
  </div>
  <div class="footer-title" style="left:784px">Follow us on</div>
  <div class="footer-rule" style="left:784px;width:226px"></div>
  <div class="social" aria-label="Social links">
    <span style="background:#1f77b4"></span>
    <span style="background:#d9452f"></span>
    <span style="background:#3b5b9a"></span>
    <span style="background:#2aa6de"></span>
    <span style="background:#f08c1e"></span>
  </div>
  <div class="copyright">Copyright © 2013 . All rights reserved.</div>
</footer>
</body>
</html>
```